Tallwood Gatherings brochure

We need a brochure designed that is modern, high impact and grabs potential customers attention. I have provided a draft mock brochure as an example and to provide the desired information. The lay out and design can be changed.

The front to include image (examples provided. I may provide other images if I can source) Logo, Joining the Community, and perhaps a Community Access and Lifestyle Support Service, Specialising in Lifestyle and Recreation

Refer to website for information on the service www.tallwoodgatherings.com.au

Use colours of logo for design

Target Market(s)

KTRV participants (People with a disability and their family)

Colors

Designer to choose colors to be used in the design.

Requirements
Must have
• Image/s of people, logo, text in mock up design. Example images provided. Will source more images and upload.
Nice to have
• More than one image

```html
<!DOCTYPE html>
<html lang="en">
<head>
<meta charset="utf-8">
<title>Tallwood Gatherings – Brochure</title>
<link href="https://fonts.googleapis.com/css2?family=Open+Sans:wght@400;600;700;800&display=swap" rel="stylesheet">
<style>
  :root{
    --page:#e9e7e3;
    --blue-deep:#1d4fa8;
    --blue-mid:#2f66c4;
    --blue-light:#5b8fdc;
    --blue-pale:#7aa9e6;
    --navy:#123a86;
    --green-dark:#0f5a2c;
    --green-mid:#2c9a3c;
    --green-light:#7cc242;
    --tree-tone:#2f5f6a;
    --white:#ffffff;
  }
  *{margin:0;padding:0;box-sizing:border-box}
  html,body{width:1200px;height:1013px;overflow:hidden;background:var(--page)}
  body{font-family:"Open Sans",sans-serif;color:var(--white)}
  .brochure{position:absolute;left:30px;top:66px;width:1140px;height:880px;overflow:hidden;
    box-shadow:0 6px 24px rgba(0,0,0,.18)}
  .panel{position:absolute;top:0;width:380px;height:880px}
  .panel--about{left:0}
  .panel--contact{left:380px;background:linear-gradient(180deg,var(--blue-deep) 0%,var(--blue-mid) 60%,var(--blue-light) 100%)}
  .panel--cover{left:760px;background:linear-gradient(180deg,var(--blue-mid) 0%,var(--blue-light) 45%,var(--blue-pale) 100%)}
  .photo-tree{position:absolute;inset:0;
    background:linear-gradient(180deg,var(--blue-deep) 0%,#24549f 35%,var(--tree-tone) 75%,#2b5a7a 100%)}
  .fold{position:absolute;top:0;width:2px;height:880px;background:linear-gradient(90deg,rgba(0,0,0,.12),rgba(255,255,255,.08));z-index:3}
  .wave{position:absolute;left:0;top:590px;width:1140px;height:290px;z-index:1}
  .about-copy{position:absolute;left:36px;top:70px;width:310px;font-size:15.5px;line-height:1.45;z-index:2}
  .about-copy p+p{margin-top:22px}
  .photo-circle{position:absolute;border-radius:50%;border:4px solid var(--white);z-index:2;
    background:linear-gradient(180deg,#4f8de0 0%,#3a7ad4 55%,#6d8a9c 100%)}
  .photo-circle--large{left:26px;top:612px;width:190px;height:190px}
  .photo-circle--small{left:206px;top:650px;width:140px;height:140px}
  .call-us{position:absolute;left:32px;bottom:34px;z-index:2;font-weight:700;font-size:25px;letter-spacing:1px;display:flex;align-items:center;gap:10px}
  .contact-copy{position:absolute;left:0;top:74px;width:380px;text-align:center;z-index:2;text-transform:uppercase}
  .contact-copy .lead{font-size:15.5px;line-height:1.55;font-weight:400}
  .contact-copy .heading{margin-top:22px;font-size:24px;font-weight:700;letter-spacing:1px}
  .contact-copy .sub{font-size:15px;letter-spacing:.5px}
  .details{position:absolute;left:0;top:330px;width:380px;text-align:center;z-index:2;font-size:12.5px;line-height:1.4}
  .details .row{margin-bottom:14px}
  .details svg{display:block;margin:0 auto 4px}
  .social{position:absolute;left:0;bottom:62px;width:380px;display:flex;justify-content:center;align-items:center;gap:10px;z-index:2;font-size:17px}
  .social .dot{width:20px;height:20px;border-radius:50%;background:var(--white)}
  .brand{position:absolute;left:70px;top:50px;display:flex;align-items:center;gap:10px;z-index:2}
  .brand .mark{width:44px;height:44px;border-radius:50%;border:3px solid var(--white)}
  .brand .name{font-size:19px;font-weight:600;line-height:1.1}
  .headline{position:absolute;left:0;top:130px;width:380px;text-align:center;z-index:2;
    font-size:38px;font-weight:800;line-height:1.05;color:var(--navy);text-transform:uppercase}
  .tagline{position:absolute;left:0;top:222px;width:380px;text-align:center;z-index:2;font-size:15px;text-transform:uppercase;line-height:1.35}
  .photo-hero{position:absolute;left:0;top:280px;width:380px;height:600px;z-index:0;
    background:linear-gradient(180deg,rgba(122,169,230,0) 0%,rgba(110,159,224,.6) 20%,#6894d0 50%,#5a7f9a 72%,#4d7a4a 90%,#4d7a4a 100%)}
  .site{position:absolute;left:0;bottom:62px;width:380px;display:flex;justify-content:center;align-items:center;gap:10px;z-index:2;font-size:16px}
</style>
</head>
<body>
<main class="brochure">
  <section class="panel panel--about">
    <div class="photo-tree" role="img" aria-label="Photo of a tall leafy tree against a clear blue sky"></div>
    <div class="about-copy">
      <p>Tallwood Gatherings Association Inc. provides people with one-on-one lifestyle support and assistance so they have opportunities to connect with their community in a valuable and genuine way.</p>
      <p>Everyone is entitled to achieve their vision of an ordinary life and have a valued role in community.</p>
      <p>Proudly founded in 1993 by Marlow parents as Parkside Leisure. Re-named Tallwood Gatherings in 2015 to reflect our expanded range of services</p>
    </div>
    <div class="photo-circle photo-circle--large" role="img" aria-label="Photo of a man in a power wheelchair with a child by the sea"></div>
    <div class="photo-circle photo-circle--small" role="img" aria-label="Photo of a wheelchair user and a child on a seaside path"></div>
    <div class="call-us">CALL US
      <svg width="24" height="20" viewBox="0 0 24 20" aria-hidden="true"><path fill="#fff" d="M2 6c0-3 5-5 10-5s10 2 10 5v2h-5V5H7v3H2zM6 9h12l3 9H3z"/></svg>
      (07) 40123456</div>
  </section>

  <section class="panel panel--contact">
    <div class="contact-copy">
      <p class="lead">For more information,<br>or<br>if you are interested in<br>receiving our services<br>or<br>becoming a support person,</p>
      <p class="heading">Please contact</p>
      <p class="sub">Tallwood Gatherings</p>
    </div>
    <div class="details">
      <div class="row">
        <svg width="12" height="16" viewBox="0 0 12 16" aria-hidden="true"><path fill="#fff" d="M6 0a6 6 0 0 0-6 6c0 4 6 10 6 10s6-6 6-10a6 6 0 0 0-6-6zm0 8.5A2.5 2.5 0 1 1 6 3.5a2.5 2.5 0 0 1 0 5z"/></svg>
        27–29 Wattle Street<br>Brookvale QLD 4879
      </div>
      <div class="row">PO Box 312<br>Brookvale QLD 4870</div>
      <div class="row">
        <svg width="14" height="12" viewBox="0 0 24 20" aria-hidden="true"><path fill="#fff" d="M2 6c0-3 5-5 10-5s10 2 10 5v2h-5V5H7v3H2zM6 9h12l3 9H3z"/></svg>
        (07) 40123456
      </div>
      <div class="row">
        <svg width="14" height="10" viewBox="0 0 14 10" aria-hidden="true"><rect x=".5" y=".5" width="13" height="9" fill="none" stroke="#fff"/><path d="M.5.5 7 6l6.5-5.5" fill="none" stroke="#fff"/></svg>
        servicemanager@tallwoodgatherings.com.au
      </div>
      <div class="row">
        <svg width="13" height="13" viewBox="0 0 14 14" aria-hidden="true"><circle cx="7" cy="7" r="6" fill="none" stroke="#fff"/><ellipse cx="7" cy="7" rx="2.6" ry="6" fill="none" stroke="#fff"/><path d="M1 7h12" stroke="#fff"/></svg>
        www.tallwoodgatherings.com.au
      </div>
    </div>
    <div class="social"><span class="dot"></span>/tallwoodgatheringsmarlow</div>
  </section>

  <section class="panel panel--cover">
    <div class="photo-hero" role="img" aria-label="Photo of a smiling man in a wheelchair and a child on skates with arms outstretched"></div>
    <div class="brand"><span class="mark"></span><span class="name">Tallwood<br>Gatherings</span></div>
    <h1 class="headline">Joining the<br>community</h1>
    <p class="tagline">A community access and<br>lifestyle support service</p>
    <div class="site">
      <svg width="16" height="16" viewBox="0 0 14 14" aria-hidden="true"><circle cx="7" cy="7" r="6" fill="none" stroke="#fff"/><ellipse cx="7" cy="7" rx="2.6" ry="6" fill="none" stroke="#fff"/><path d="M1 7h12" stroke="#fff"/></svg>
      www.tallwoodgatherings.com.au
    </div>
  </section>

  <svg class="wave" viewBox="0 0 1140 290" preserveAspectRatio="none" aria-hidden="true">
    <path fill="var(--green-light)" d="M0 40 C300 0 560 120 760 110 C900 100 1020 40 1140 0 L1140 40 C1020 80 900 140 760 150 C560 160 300 50 0 80Z"/>
    <path fill="var(--green-mid)" d="M0 70 C300 40 560 150 760 140 C900 130 1020 70 1140 30 L1140 60 C1020 100 900 165 760 175 C560 185 300 80 0 105Z"/>
    <path fill="var(--green-dark)" d="M0 100 C300 75 560 180 760 170 C900 160 1020 95 1140 55 L1140 290 L0 290Z"/>
  </svg>

  <div class="fold" style="left:379px"></div>
  <div class="fold" style="left:759px"></div>
</main>
</body>
</html>
```